banner ad

We're looking for a banner similar to the one shown on the attached file. The same 4 keywords, the same text up top, but with new formatting, design and perhaps color scheme. Looking for something to catch people's attention that will stand out on this particular page shown in the attached image. Our goal is to find a banner with a better click through rate than the current version.

```html
<!DOCTYPE html>
<html lang="en">
<head>
<meta charset="utf-8">
<title>Blood glucose ad banner</title>
<link rel="stylesheet" href="https://fonts.googleapis.com/css2?family=Fresca&display=swap">
<style>
  :root {
    --panel-red: #e41e26;
    --panel-red-light: #f2333a;
    --panel-red-dark: #8f0f14;
    --panel-edge: #6e0a0e;
    --button-blue-top: #7fd3f2;
    --button-blue-mid: #2aaee0;
    --button-blue-deep: #0b86c4;
    --button-edge: #05618f;
    --label-yellow: #f4f70e;
    --ribbon-light: #ff8a4a;
    --ribbon-dark: #e0451c;
    --chevron: #b5211a;
    --white: #ffffff;
  }
  * { box-sizing: border-box; margin: 0; padding: 0; }
  html, body {
    width: 1200px;
    height: 275px;
    overflow: hidden;
    background: #ffffff;
  }
  .ad-banner {
    position: relative;
    width: 1200px;
    height: 275px;
  }
  .ad-banner__frame {
    position: absolute;
    inset: 0;
  }
  .ad-banner__heading {
    position: absolute;
    left: 75px;
    top: 26px;
    font-family: Arial, Helvetica, sans-serif;
    font-size: 21px;
    color: var(--white);
  }
  .ad-banner__tag {
    position: absolute;
    right: 58px;
    top: 32px;
    font-family: Arial, Helvetica, sans-serif;
    font-size: 11px;
    letter-spacing: 0.2px;
    color: var(--white);
  }
  .ad-link {
    position: absolute;
    width: 500px;
    height: 80px;
    border-radius: 8px;
    border: 2px solid var(--button-edge);
    background:
      linear-gradient(180deg, rgba(255,255,255,0.45) 0%, rgba(255,255,255,0.12) 48%, rgba(255,255,255,0) 50%),
      linear-gradient(180deg, var(--button-blue-top) 0%, var(--button-blue-mid) 45%, var(--button-blue-deep) 70%, var(--button-blue-mid) 100%);
    box-shadow: 0 2px 3px rgba(60,0,0,0.45);
    display: flex;
    align-items: center;
    justify-content: center;
    white-space: nowrap;
    text-decoration: none;
    font-family: "Fresca", sans-serif;
    font-size: 38px;
    letter-spacing: -0.3px;
    color: var(--label-yellow);
    text-shadow: 0 1px 1px rgba(0,50,90,0.5);
  }
  .ad-link--top { top: 73px; }
  .ad-link--bottom { top: 170px; }
  .ad-link--left { left: 82px; }
  .ad-link--right { left: 632px; }
  .ad-link--glucose { padding-left: 40px; }
  .ad-link--range { padding-left: 90px; }
  .ad-link--chart { padding-right: 70px; }
  .ad-link--normal { justify-content: flex-start; padding-left: 3px; }
  .ribbon {
    position: absolute;
    width: 110px;
    height: 56px;
  }
</style>
</head>
<body>
<div class="ad-banner">
  <svg class="ad-banner__frame" width="1200" height="275" viewBox="0 0 1200 275" aria-hidden="true">
    <defs>
      <linearGradient id="frameEdge" x1="0" y1="0" x2="1" y2="0">
        <stop offset="0" stop-color="#fbe5e5"/>
        <stop offset="0.03" stop-color="#7a0b10"/>
        <stop offset="0.5" stop-color="#b01419"/>
        <stop offset="0.97" stop-color="#7a0b10"/>
        <stop offset="1" stop-color="#fbe5e5"/>
      </linearGradient>
      <linearGradient id="panelFill" x1="0" y1="0" x2="0" y2="1">
        <stop offset="0" stop-color="#f5343b"/>
        <stop offset="0.5" stop-color="#e41e26"/>
        <stop offset="1" stop-color="#c8161d"/>
      </linearGradient>
    </defs>
    <path d="M0 10 Q0 2 20 2 L1180 2 Q1200 2 1200 10 L1200 255 Q1200 273 1182 273 L18 273 Q0 273 0 255 Z" fill="url(#frameEdge)"/>
    <path d="M28 8 L1172 8 Q1190 8 1190 40 L1190 250 Q1190 264 1176 264 L24 264 Q10 264 10 250 L10 40 Q10 8 28 8 Z" fill="url(#panelFill)"/>
    <path d="M10 250 Q10 264 24 264 L1176 264 Q1190 264 1190 250 L1190 258 Q1190 270 1176 270 L24 270 Q10 270 10 258 Z" fill="#6e0a0e"/>
  </svg>

  <p class="ad-banner__heading">Ads Related to blood glucose</p>
  <p class="ad-banner__tag">ADVERTISEMENT</p>

  <a class="ad-link ad-link--left ad-link--top ad-link--glucose" href="#">Blood Glucose</a>
  <a class="ad-link ad-link--right ad-link--top ad-link--chart" href="#">Blood Sugar Levels Chart</a>
  <a class="ad-link ad-link--left ad-link--bottom ad-link--range" href="#">Normal Blood Sugar Range</a>
  <a class="ad-link ad-link--right ad-link--bottom ad-link--normal" href="#">What is Normal Blood Sugar</a>

  <svg class="ribbon" style="left:66px;top:85px" viewBox="0 0 110 56" aria-hidden="true">
    <polygon points="0,3 82,3 108,28 82,53 0,53" fill="#e0451c"/>
    <polygon points="0,3 82,3 108,28 0,28" fill="#ff8a4a"/>
    <polyline points="74,14 92,28 74,42" fill="none" stroke="#b5211a" stroke-width="7" stroke-linejoin="round"/>
  </svg>
  <svg class="ribbon" style="left:66px;top:182px" viewBox="0 0 110 56" aria-hidden="true">
    <polygon points="0,3 82,3 108,28 82,53 0,53" fill="#e0451c"/>
    <polygon points="0,3 82,3 108,28 0,28" fill="#ff8a4a"/>
    <polyline points="74,14 92,28 74,42" fill="none" stroke="#b5211a" stroke-width="7" stroke-linejoin="round"/>
  </svg>
  <svg class="ribbon" style="left:1040px;top:85px" viewBox="0 0 110 56" aria-hidden="true">
    <polygon points="110,3 28,3 2,28 28,53 110,53" fill="#e0451c"/>
    <polygon points="110,3 28,3 2,28 110,28" fill="#ff8a4a"/>
    <polyline points="36,14 18,28 36,42" fill="none" stroke="#b5211a" stroke-width="7" stroke-linejoin="round"/>
  </svg>
  <svg class="ribbon" style="left:1040px;top:182px" viewBox="0 0 110 56" aria-hidden="true">
    <polygon points="110,3 28,3 2,28 28,53 110,53" fill="#e0451c"/>
    <polygon points="110,3 28,3 2,28 110,28" fill="#ff8a4a"/>
    <polyline points="36,14 18,28 36,42" fill="none" stroke="#b5211a" stroke-width="7" stroke-linejoin="round"/>
  </svg>
</div>
</body>
</html>
```